Sunvale Hearth Roti/Naan bread packaging for Australia

We would like to update and refresh the packaging design for our Sunvale Hearth bread range. These breads are currently being sold in Australian supermarkets and are very popular. The proposed design should have some "continuity" with the current packaging design so that consumers can still recognise the brand/product easily on shelf. The design should suggest "fresh, tasty, healthy, authentic and Australian-made".
FYI, the products are not chilled or frozen - they sit on the regular supermarket shelves and will need to stand out. The breads will typically sit next to each other on the shelf, but usually just one facing each. I'll be uploading image files of the current packaging for your reference.
Updates

Hi all, I just uploaded the current logo for those of you who want it.  Also, there are printer details in the discussion area that you might find useful.  I am hoping to get their design template in the next day or so, but don't let that stop you from starting.  We are only looking for a design concept that we can use across the product range.  Cheers!

Hi, I've uploaded the design template/layers for those who would like this.  Cheers!

Hi everyone, thanks to those of you who have either submitted or are working on designs.  I have reviewed the available designs with the MD and will be providing individual feedback to you wherever possible.

Lastly, we'll be extending the deadline for a few more days to allow for changes and resubmissions.

Good luck everyone!

Reason: To allow for changes and resubmissions - will be providing individual feedback to all designs submitted. Cheers.

Reason: One last extension before we award the guaranteed prize.

Target Market(s)

Australian consumers who eat Indian foods and would pay a premium for a better product

Industry/Entity Type

Product

Requirements
Must have
• Transparent window to show breads
Some carryover elements from current packaging for consumer recognition
Same product info on the back (i.e. Nutritional Info panel, Heating Instructions, Barcode, Company details, Usage Suggestions)
Nice to have
• The design should suggest "fresh, tasty, healthy, authentic and Australian-made".

```html
<!DOCTYPE html>
<html lang="en">
<head>
<meta charset="utf-8">
<title>Sunvale Hearth Garlic Naan – pack layout</title>
<link rel="stylesheet" href="https://fonts.googleapis.com/css2?family=Lato:wght@400;700;900&family=Sriracha&display=swap">
<style>
:root{
  --pack-yellow:#fcc636;
  --panel-yellow:#fdd04e;
  --orange:#ec6f1f;
  --orange-text:#f07d1e;
  --rule:#f3a44a;
  --purple:#6b3fa0;
  --grey:#d3d4d6;
  --dim-line:#777;
  --white:#ffffff;
  --ink:#222;
}
*{box-sizing:border-box;margin:0;padding:0}
html,body{width:1200px;height:823px;overflow:hidden;background:#fff}
body{position:relative;font-family:"Lato",Arial,sans-serif;color:var(--ink)}
.abs{position:absolute}

/* dimension guides */
.dims{left:0;top:0;width:1200px;height:66px}
.dim-label{position:absolute;font-size:11px;color:#333;transform:translateX(-50%)}
.dim-vert{left:10px;top:66px;width:1px;height:757px;background:var(--dim-line)}
.dim-vert::before{content:"";position:absolute;left:-4px;top:0;width:9px;height:1px;background:var(--dim-line)}

/* artwork */
.bleed{top:66px;height:757px;background:var(--grey)}
.bleed-left{left:28px;width:80px}
.bleed-right{left:1114px;width:86px}
.pack{left:108px;top:66px;width:1006px;height:757px;background:var(--pack-yellow)}

.side-panel{top:145px;width:210px;height:618px;border:2px solid var(--orange);border-radius:10px;background:var(--panel-yellow);padding:0 10px;overflow:hidden}
.panel-left{left:131px}
.panel-right{left:884px}

.brand{font-family:"Lato",Arial,sans-serif;font-weight:900;color:var(--purple);text-align:center;white-space:nowrap}
.brand-small{font-size:15px;margin-top:18px;line-height:1.1}
.brand-small span,.brand-main span{display:block}
.brand-main{left:523px;top:183px;width:174px;font-size:30px;line-height:1.05}

.variant{font-weight:700;color:var(--orange-text);font-size:19px;letter-spacing:1px;text-align:center;margin-top:20px;white-space:nowrap}

/* nutrition */
.nutrition{margin-top:6px;border:1px solid var(--rule);font-size:9px;background:var(--panel-yellow)}
.nutrition h3{font-size:11.5px;font-weight:700;color:var(--purple);padding:3px 4px;border-bottom:1px solid var(--rule);white-space:nowrap}
.nutrition .serving{padding:2px 5px;font-size:9.5px;line-height:1.15;border-bottom:1px solid var(--rule)}
.nutrition table{width:100%;border-collapse:collapse}
.nutrition th{font-weight:400;font-size:7px;padding:2px 1px;border-left:1px solid var(--rule);border-bottom:1px solid var(--rule);text-align:center;line-height:1.1;white-space:nowrap}
.nutrition th:first-child{border-left:none}
.nutrition td{padding:0 4px;line-height:1.2;font-size:8.5px;white-space:nowrap}
.nutrition td+td{border-left:1px solid var(--rule);text-align:center;padding:0 2px}
.nutrition tbody tr:first-child td{padding-top:9px}
.nutrition tbody tr:last-child td{padding-bottom:4px}
.nutrition .cal{font-size:6px}

.block-title{font-size:12.5px;color:var(--ink);margin-top:12px}
.orange-copy{color:var(--orange-text)}
.ingredients p{font-size:12px;line-height:15.3px}

.maker{margin-top:22px;padding-left:3px;font-size:12.5px;line-height:15.3px;position:relative}
.map-mark{position:absolute;left:136px;top:58px;width:36px;height:28px;background:var(--orange);border-radius:5px 12px 10px 14px}

.heating h2{font-size:15.5px;font-weight:700;color:var(--purple);line-height:1.2;margin-top:12px}
.heating p{font-size:12.5px;line-height:15.3px;margin-top:8px;color:var(--ink)}
.heating p span{color:var(--orange-text)}

.barcode-panel{left:912px;top:632px;width:156px;height:103px;background:var(--white)}
.barcode-panel::after{content:"";position:absolute;left:16px;top:9px;width:122px;height:75px;background:var(--grey)}

/* front face */
.tagline{left:360px;top:302px;width:502px;text-align:center;font-family:"Sriracha",cursive;font-size:29px;color:var(--purple)}
.product{left:360px;top:352px;width:502px;text-align:center;font-weight:900;font-size:82px;line-height:1;color:var(--white);-webkit-text-stroke:3px var(--orange);paint-order:stroke fill;letter-spacing:2px}

.window-band{left:360px;width:502px;background:var(--orange)}
.band-top{top:442px;height:10px}
.band-bottom{top:688px;height:10px}
.window{left:360px;top:456px;width:502px;height:229px;background:var(--grey);border-top:2px solid var(--white);border-bottom:2px solid var(--white)}

.count{left:700px;top:606px;height:46px;display:flex}
.count-num{width:46px;height:46px;background:var(--orange);color:var(--white);font-weight:900;font-size:44px;line-height:46px;text-align:center}
.count-label{border:2px solid var(--orange);border-left:none;padding:4px 6px 0;color:var(--orange);font-weight:900;font-size:17px;line-height:.98;letter-spacing:1px}

.serve-line{left:515px;top:702px;font-family:"Sriracha",cursive;font-size:28px;color:var(--purple)}
.serve-line u{text-decoration-thickness:1px;text-underline-offset:4px}
.net{left:740px;top:717px;font-size:20px;color:var(--white)}
</style>
</head>
<body>

<div class="abs dims" aria-hidden="true">
  <svg width="1200" height="66" viewBox="0 0 1200 66">
    <g stroke="#777" stroke-width="1" fill="none">
      <line x1="28" y1="22.5" x2="1200" y2="22.5"/>
      <line x1="28" y1="46.5" x2="1200" y2="46.5"/>
      <line x1="28.5" y1="18" x2="28.5" y2="52"/>
      <line x1="108.5" y1="42" x2="108.5" y2="52"/>
      <line x1="360.5" y1="42" x2="360.5" y2="52"/>
      <line x1="862.5" y1="42" x2="862.5" y2="52"/>
      <line x1="1114.5" y1="42" x2="1114.5" y2="52"/>
    </g>
  </svg>
  <span class="dim-label" style="left:612px;top:2px">420</span>
  <span class="dim-label" style="left:68px;top:30px">30</span>
  <span class="dim-label" style="left:234px;top:30px">90</span>
  <span class="dim-label" style="left:612px;top:30px">180</span>
  <span class="dim-label" style="left:980px;top:30px">90</span>
  <span class="dim-label" style="left:1157px;top:30px">30</span>
</div>
<div class="abs dim-vert" aria-hidden="true"></div>

<div class="abs bleed bleed-left"></div>
<div class="abs bleed bleed-right"></div>
<div class="abs pack" role="img" aria-label="Warm yellow background with a soft repeating motif"></div>

<!-- back left: nutrition, ingredients, maker -->
<section class="abs side-panel panel-left">
  <div class="brand brand-small"><span>Sunvale</span><span>Hearth</span></div>
  <div class="variant">GARLIC NAAN</div>
  <div class="nutrition">
    <h3>NUTRITIONAL INFORMATION</h3>
    <div class="serving">SERVINGS PER PACK: 4<br>SERVING SIZE: 70g</div>
    <table>
      <thead><tr><th></th><th>Average quantity<br>per serving</th><th>Average quantity<br>per 100g</th></tr></thead>
      <tbody>
        <tr><td>Energy</td><td>910KJ <span class="cal">(217Cal)</span></td><td>1300KJ <span class="cal">(311Cal)</span></td></tr>
        <tr><td>Protein</td><td>5.7g</td><td>8.1g</td></tr>
        <tr><td>Fat, Total</td><td>5.7g</td><td>8.1g</td></tr>
        <tr><td>&nbsp;- Saturated</td><td>2.4g</td><td>3.4g</td></tr>
        <tr><td>Carbohydrate</td><td>34.7g</td><td>49.5g</td></tr>
        <tr><td>&nbsp;- Sugar</td><td>3.0g</td><td>4.3g</td></tr>
        <tr><td>Sodium</td><td>404mg</td><td>579mg</td></tr>
      </tbody>
    </table>
  </div>
  <div class="ingredients">
    <div class="block-title">INGREDIENTS:</div>
    <p class="orange-copy">Wheat Flour, (Folic Acid, Thiamin), Water, Vegetable Oils [antioxidant 306 (from Soy) or 320, 319], Sugar, Gluten, Yoghurt Powder, Iodised Salt, Humectant (422), Mineral Salts (500, 450), Food Acid (297, 200), Cultured Dextrose, Vinegar, Yeast, Preservative (282, 202), Vegetable Gum (412), Emulsifier (481, 472e), Corn Starch, Nigella Seeds.</p>
  </div>
  <div class="maker">
    MADE IN AUSTRALIA<br>
    <span class="orange-copy">Ridgeway Bakehouse Pty Ltd<br>14 Wattlebank Road<br>Brookvale Park 3077<br>VICTORIA</span><br>
    T:&nbsp; 03 9000 4812<br>
    E:&nbsp; <span class="orange-copy">hi@ridgewaybake.com.au</span>
    <div class="map-mark" role="img" aria-label="Map of Australia"></div>
  </div>
</section>

<!-- front face -->
<div class="abs brand brand-main"><span>Sunvale</span><span>Hearth</span></div>
<div class="abs tagline">Authentic Garlic</div>
<div class="abs product">NAAN</div>
<div class="abs window-band band-top"></div>
<div class="abs window" role="img" aria-label="Clear window showing the naan breads"></div>
<div class="abs window-band band-bottom"></div>
<div class="abs count">
  <div class="count-num">4</div>
  <div class="count-label">PER<br>PACK</div>
</div>
<div class="abs serve-line">Just <u>heat</u> &amp; <u>eat</u>!</div>
<div class="abs net">250g net</div>

<!-- back right: heating -->
<section class="abs side-panel panel-right heating">
  <div class="brand brand-small"><span>Sunvale</span><span>Hearth</span></div>
  <div class="variant">GARLIC NAAN</div>
  <h2>HEATING<br>INSTRUCTIONS</h2>
  <p>CONVENTIONAL OVEN:<br><span>Preheat oven to 200°C. Remove all packaging. Sprinkle the Naan with water and wrap in foil. Place on a baking tray on the middle oven shelf and heat for 10 minutes.</span></p>
  <p>GRILL: <span>Preheat the grill to the moderate heat. Remove Naan breads from packaging and place on grill pan. Sprinkle with water and grill for 2 minutes, turning once.</span></p>
  <p>MICROWAVE: <span>Microwave each Naan for 30 seconds on high.</span></p>
</section>
<div class="abs barcode-panel" role="img" aria-label="Barcode area"></div>

</body>
</html>
```